Project: Business Card Design
Business Card Design - Information
Business Card Design
Use specific fonts
Does not matter
Professional
Colin Marsh
President
4817 Thornbury Lane
cm@supplyvetta.com
www.supplyvetta.com
See supplyvetta.com for existing design. We want to business card to match or compliment the existing website.
Get Ready. Your Vendor Selection and Management Processes Are Changing. SupplyVettaā„¢ is a highly effective process that gathers key information about your vendors so you can confidently make decisions to hire those who best meet your needs and expectations.

```html
<!DOCTYPE html>
<html lang="en">
<head>
<meta charset="utf-8">
<title>SupplyVetta Business Card</title>
<link rel="stylesheet" href="https://fonts.googleapis.com/css2?family=Open+Sans:wght@400;600;700;800&display=swap">
<style>
  :root {
    --green: #3f9a2c;
    --green-dark: #2a7a1c;
    --green-light: #6cc04a;
    --charcoal: #3a3a3a;
    --grey: #6b6b6b;
    --paper: #ffffff;
    --backdrop: #e6e3dd;
  }
  * { box-sizing: border-box; margin: 0; padding: 0; }
  html, body {
    width: 1200px; height: 901px; overflow: hidden;
    background: var(--backdrop);
    font-family: "Open Sans", Arial, sans-serif;
  }
  .sheet {
    width: 1200px; height: 901px;
    display: flex; align-items: center; justify-content: center; gap: 60px;
  }
  .card {
    position: relative; width: 520px; height: 297px; overflow: hidden;
    box-shadow: 0 6px 18px rgba(0,0,0,.18);
  }
  .card-front { background: var(--paper); }
  .card-front .swoosh { position: absolute; inset: 0; }
  .brand {
    position: absolute; left: 30px; top: 40px;
    display: flex; align-items: center; gap: 10px;
  }
  .brand-mark {
    width: 38px; height: 38px; background: var(--green); border-radius: 4px;
  }
  .brand-name {
    font-weight: 800; font-size: 28px; letter-spacing: -0.5px;
    color: var(--charcoal); line-height: 1;
  }
  .tagline {
    position: absolute; left: 80px; top: 80px;
    font-size: 10px; color: var(--green); font-weight: 600;
  }
  .person { position: absolute; left: 30px; top: 150px; }
  .person-name { font-size: 22px; color: var(--green); font-weight: 400; }
  .person-title { font-size: 11px; color: var(--grey); margin-top: 2px; }
  .contact {
    position: absolute; left: 330px; top: 150px;
    font-size: 10.5px; color: var(--charcoal); line-height: 1.75;
    list-style: none;
  }
  .contact li { display: flex; align-items: center; gap: 6px; }
  .contact .icon { width: 10px; height: 10px; flex: none; }
  .contact .address { margin-bottom: 2px; font-weight: 600; }

  .card-back {
    background: linear-gradient(135deg, var(--green-light) 0%, var(--green) 45%, var(--green-dark) 100%);
    color: var(--paper);
  }
  .back-mark {
    position: absolute; left: 50px; top: 100px;
    width: 96px; height: 96px; background: var(--paper); border-radius: 10px;
  }
  .back-copy { position: absolute; left: 190px; top: 70px; width: 295px; }
  .back-heading { font-size: 22px; font-weight: 700; margin-bottom: 10px; }
  .back-lead { font-size: 11.5px; font-weight: 600; margin-bottom: 8px; line-height: 1.4; }
  .back-body { font-size: 10.5px; line-height: 1.5; opacity: .95; }
</style>
</head>
<body>
<main class="sheet">
  <section class="card card-front" aria-label="Card front">
    <svg class="swoosh" width="520" height="297" viewBox="0 0 520 297" aria-hidden="true">
      <path d="M0 215 C120 200 220 215 290 262 C320 282 345 297 360 297 L0 297 Z" fill="var(--green)"/>
      <path d="M0 205 C125 190 230 205 300 255 C330 276 355 292 375 297" fill="none" stroke="var(--charcoal)" stroke-width="3"/>
      <path d="M300 0 C360 50 410 100 520 115 L520 0 Z" fill="var(--green)"/>
      <path d="M285 0 C345 55 400 110 520 128" fill="none" stroke="var(--charcoal)" stroke-width="3"/>
    </svg>
    <div class="brand">
      <span class="brand-mark"></span>
      <span class="brand-name">SUPPLYVETTA</span>
    </div>
    <p class="tagline">Smarter vendor decisions</p>
    <div class="person">
      <p class="person-name">Colin Marsh</p>
      <p class="person-title">President</p>
    </div>
    <ul class="contact">
      <li class="address">4817 Thornbury Lane</li>
      <li><svg class="icon" viewBox="0 0 10 10"><circle cx="5" cy="5" r="5" fill="var(--charcoal)"/><path d="M3 2.5h1.2l.5 1.5-.8.6a4 4 0 0 0 1.5 1.5l.6-.8 1.5.5v1.2c-3 .3-4.8-1.5-4.5-4.5z" fill="#fff"/></svg>T: 555-014-2297</li>
      <li><svg class="icon" viewBox="0 0 10 10"><circle cx="5" cy="5" r="5" fill="var(--charcoal)"/><rect x="2.5" y="3.5" width="5" height="3.5" fill="#fff"/></svg>F: 555-014-2298</li>
      <li><svg class="icon" viewBox="0 0 10 10"><circle cx="5" cy="5" r="5" fill="var(--charcoal)"/><path d="M2.5 3.5h5v3.5h-5z M2.5 3.5l2.5 2 2.5-2" fill="none" stroke="#fff" stroke-width=".8"/></svg>cm@supplyvetta.com</li>
      <li><svg class="icon" viewBox="0 0 10 10"><circle cx="5" cy="5" r="5" fill="var(--charcoal)"/><circle cx="5" cy="5" r="2.6" fill="none" stroke="#fff" stroke-width=".8"/><path d="M2.4 5h5.2" stroke="#fff" stroke-width=".8"/></svg>www.supplyvetta.com</li>
    </ul>
  </section>

  <section class="card card-back" aria-label="Card back">
    <span class="back-mark"></span>
    <div class="back-copy">
      <h2 class="back-heading">Be Prepared!</h2>
      <p class="back-lead">A clearer way to choose and manage the suppliers you rely on.</p>
      <p class="back-body">SupplyVetta™ collects the facts that matter about each supplier, so your team can compare options with confidence and pick partners that fit your goals, budget and standards.</p>
    </div>
  </section>
</main>
</body>
</html>
```